Business card and Logo for a Harbour Stone Rise

We need a business card and logo for a Harbour Stone Rise.

The studios name is "Harbour Stone Rise"
Main coloring to be a bright light blue. Looking for a crisp modern look

The front of the card is to have the

Studios name.
The Logo
Harbour Stone Rise
Kim Larden
0452 614 298

The back of the card is to have a lot of words relating to the services we offer. Please place the words vertically and horizontally using different fonts, different text sizes, different boldness and different colors to create a word picture.

Main words that need highlighting are

QVK, PILATES, BOXING, SPIN, STRENGTH, WEIGHT LOSS, BALANCE

Other words to add to the mix with less emphasis

Fitness, Conditioning, Lifestyle, Wellness, Health, Energy, Cardio, Goals, Muscle Tone, Vitality, Confidence, Attitude, Determination, Motivation, Dedication, Fun

Target Market(s)

Woman aged 30 to 60

Industry/Entity Type

Personal Trainer

Contact Information for Business Card

Harbour Stone Rise
Kim Larden
0452 614 298

Colors
0493ce
33a6d7
85cae6

```html
<!DOCTYPE html>
<html lang="en">
<head>
<meta charset="utf-8">
<title>Harbour Stone Rise – Business Card</title>
<link href="https://fonts.googleapis.com/css2?family=Open+Sans:wght@400;600;700&display=swap" rel="stylesheet">
<style>
  :root {
    --blue-bright: #0493ce;
    --blue-mid: #33a6d7;
    --blue-light: #85cae6;
    --blue-deep: #0a6fb0;
    --paper: #ffffff;
    --ink-white: #ffffff;
    --edge: #2a2a2a;
  }
  html, body {
    margin: 0;
    padding: 0;
    width: 1200px;
    height: 1110px;
    overflow: hidden;
    background: var(--paper);
    font-family: "Open Sans", Arial, sans-serif;
  }
  .canvas {
    position: relative;
    width: 1200px;
    height: 1110px;
  }
  .card {
    position: absolute;
    left: 249px;
    width: 697px;
    height: 388px;
    background: var(--paper);
    outline: 1.5px solid var(--edge);
    box-shadow: 8px 9px 12px rgba(0, 0, 0, 0.38);
    overflow: hidden;
  }
  .card--front { top: 129px; }
  .card--back { top: 582px; height: 386px; }

  /* Front */
  .front__accent-stripe {
    position: absolute;
    left: 343px; top: 0;
    width: 16px; height: 100%;
    background: var(--blue-light);
  }
  .front__panel {
    position: absolute;
    left: 359px; top: 0;
    width: 338px; height: 100%;
    background: var(--blue-bright);
  }
  .pattern-area {
    position: absolute;
    top: 0; right: 0;
    width: 301px; height: 200px;
    background: linear-gradient(200deg, var(--blue-deep) 0%, #0782c3 45%, rgba(4, 147, 206, 0) 100%);
  }
  .front__notch {
    position: absolute;
    left: 323px; top: 305px;
  }
  .brand {
    position: absolute;
    left: 34px; top: 62px;
    display: flex;
    align-items: center;
    gap: 12px;
  }
  .brand__mark {
    width: 50px; height: 50px;
    border-radius: 50%;
    background: var(--blue-bright);
  }
  .brand__name {
    font-weight: 700;
    font-size: 22px;
    color: var(--blue-bright);
    letter-spacing: 0.3px;
  }
  .person-name {
    position: absolute;
    left: 88px; top: 296px;
    margin: 0;
    font-weight: 700;
    font-size: 40px;
    line-height: 1;
    color: var(--blue-bright);
  }
  .phone {
    position: absolute;
    left: 436px; top: 316px;
    font-size: 22px;
    line-height: 1;
    letter-spacing: 3.3px;
    color: var(--ink-white);
  }

  /* Back */
  .back__band {
    position: absolute;
    left: 0; top: 0;
    width: 100%; height: 248px;
    background: var(--blue-bright);
  }
  .back__band .pattern-area { height: 198px; }
  .service {
    position: absolute;
    font-weight: 600;
    font-size: 20px;
    line-height: 1;
    color: var(--ink-white);
    letter-spacing: 0.2px;
  }
  .keywords {
    position: absolute;
    left: 0; top: 287px;
    width: 100%;
    margin: 0;
    text-align: center;
    font-size: 16px;
    line-height: 19.5px;
    letter-spacing: 2.1px;
    color: var(--blue-bright);
  }
</style>
</head>
<body>
<div class="canvas">

  <section class="card card--front" aria-label="Card front">
    <div class="front__accent-stripe"></div>
    <div class="front__panel">
      <div class="pattern-area" role="img" aria-label="Scattered overlapping blue diamond pattern"></div>
    </div>
    <svg class="front__notch" width="22" height="44" viewBox="0 0 22 44" aria-hidden="true">
      <polygon points="0,22 20,0 20,44" fill="var(--blue-light)"/>
    </svg>
    <div class="brand">
      <div class="brand__mark"></div>
      <span class="brand__name">Harbour Stone Rise</span>
    </div>
    <h1 class="person-name">Kim Larden</h1>
    <div class="phone">0452 614 298</div>
  </section>

  <section class="card card--back" aria-label="Card back">
    <div class="back__band">
      <div class="pattern-area" role="img" aria-label="Scattered overlapping blue diamond pattern"></div>
      <span class="service" style="left:67px; top:33px;">QVK</span>
      <span class="service" style="left:106px; top:56px;">PILATES</span>
      <span class="service" style="left:177px; top:78px;">BOXING</span>
      <span class="service" style="left:253px; top:101px;">SPIN</span>
      <span class="service" style="left:301px; top:123px;">STRENGTH</span>
      <span class="service" style="left:406px; top:146px;">WEIGHT LOSS</span>
      <span class="service" style="left:543px; top:168px;">BALANCE</span>
    </div>
    <p class="keywords">
      Fitness, Conditioning, Lifestyle, Wellness, Health, Energy<br>
      Cardio, Goals, Muscle Tone, Vitality, Confidence, Attitude<br>
      Determination, Motivation, Dedication, Fun
    </p>
  </section>

</div>
</body>
</html>
```